8 Page Publishing/Entertainment Website Design

We need a slick, polished, professional looking fully mobile responsive website designed for the publishing / entertainment industry. It will contain 8 pages, including the Home page. The site is to be designed in pure HTML and CSS only and to be compatible with any type of server we put it on. Pages are *not* to be part of any template system, like WordPress or others like it. Pure HTML and CSS standalone pages only. No WordPress or Joomla, etc. Website to use our logo's colors of red/white throughout its design. Uploaded files contain a word DOC that outlines more of our needs and we have included our logo file. Please read the specifications in the Word Document attached. We have also included a PDF file with the website specs as well.

Target Market(s)

Authors and Screenwriters

Coding

Coded - Design and coding required

Number of Pages Required

5+ page

Colors
ec1f27
ffffff
f04a50
f59195

Requirements
Must have
• The site is to be designed in pure HTML and CSS only and to be compatible with any type of server we put it on. Pages are *not* to be part of any template system, like WordPress or others like it. Pure HTML and CSS standalone pages only. No WordPress or Joomla, etc. Website to use our logo's colors of red/white throughout its design. Uploaded files contain a word DOC that outlines more of our needs and we have included our logo file. Please read the specifications in the Word Document attached. We have also included a PDF file with the website specs as well.
Should not have
• No Wordpress or other Template type pages. Pure HTML and CSS only. Some Javascript and JQuery is okay, upon approval.

```html
<!DOCTYPE html>
<html lang="en">
<head>
<meta charset="utf-8">
<title>Redline Publishing</title>
<link href="https://fonts.googleapis.com/css2?family=Nunito+Sans:wght@400;600;700;800;900&display=swap" rel="stylesheet">
<style>
:root{
  --red:#ec1f27;
  --red-mid:#f04a50;
  --red-soft:#f59195;
  --white:#ffffff;
  --ink:#222222;
  --text:#4a4a4a;
  --grey-band:#f4f4f4;
  --bar-grey:#8a8a8a;
  --footer:#1e1e1e;
  --footer-text:#9a9a9a;
}
*{margin:0;padding:0;box-sizing:border-box}
html,body{width:1200px;height:3309px;overflow:hidden;background:var(--white)}
body{font-family:"Nunito Sans",Arial,sans-serif;color:var(--text);position:relative}
.btn{position:absolute;display:flex;align-items:center;justify-content:center;width:200px;height:42px;font-weight:700;font-size:15px;letter-spacing:.5px;text-transform:uppercase}
.btn-red{background:var(--red);color:var(--white)}
.btn-outline{border:2px solid var(--ink);color:var(--ink);background:transparent}
.btn-white{background:var(--white);color:var(--red)}

/* header */
.site-header{position:absolute;top:0;left:0;width:1200px;height:93px;background:var(--white);display:flex;align-items:center;padding:0 88px}
.brand{display:flex;align-items:center;gap:10px;font-weight:900;font-size:20px;color:var(--red);text-transform:uppercase}
.brand-dot{width:40px;height:40px;border-radius:50%;background:var(--red)}
.main-nav{margin-left:auto;display:flex;gap:22px;font-size:13.5px;font-weight:600;color:var(--ink);text-transform:uppercase}
.main-nav .active{color:var(--red)}

/* hero */
.hero{position:absolute;top:93px;left:0;width:1200px;height:553px;background:linear-gradient(180deg,#6f8193 0%,#c9cfd4 30%,#9aa2a6 60%,#3a3527 85%,#1c1a14 100%)}
.hero-title{position:absolute;top:50px;width:100%;text-align:center;color:var(--white);font-weight:800;font-size:42px;letter-spacing:.5px}
.hero-video{position:absolute;left:353px;top:119px;width:496px;height:302px;border:4px solid var(--red);background:linear-gradient(180deg,#e9ecee,#d6dadd);display:flex;align-items:center;justify-content:center;gap:12px;font-weight:900;font-size:24px;color:var(--red);text-transform:uppercase}
.hero-video .brand-dot{width:56px;height:56px}
.hero .btn{left:501px;top:450px}

/* heading */
.section-heading{position:absolute;left:0;width:1200px;display:flex;align-items:center;justify-content:center;gap:18px;font-weight:800;font-size:32px;color:var(--ink);text-transform:uppercase}
.section-heading::before,.section-heading::after{content:"";width:96px;height:3px;background:var(--ink)}
.lead-red{position:absolute;left:0;width:1200px;text-align:center;color:var(--red);font-size:13px;font-weight:600}

/* about */
.about{position:absolute;top:646px;left:0;width:1200px;height:431px}
.about .section-heading{top:80px}
.about .lead-red{top:130px}
.about-copy{position:absolute;top:158px;left:220px;width:762px;text-align:center;font-size:13px;line-height:24px}
.about .btn{left:501px;top:300px}

/* featured book */
.featured{position:absolute;top:1077px;left:0;width:1200px;height:485px;background:var(--grey-band)}
.book-visual{position:absolute;left:88px;top:75px;width:497px;height:324px;background:linear-gradient(90deg,#f6c9c0 0%,#8d4a6a 22%,#ffffff 34%,#ececec 70%,#f4d5de 100%);box-shadow:0 6px 18px rgba(0,0,0,.2)}
.featured-title{position:absolute;left:638px;top:124px;font-size:22px;font-weight:700;color:var(--red)}
.featured-copy{position:absolute;left:640px;top:158px;width:470px;font-size:13px;line-height:25px}
.featured-copy a{color:var(--red);text-decoration:underline}
.featured .btn{left:640px;top:302px}

/* authors */
.authors{position:absolute;top:1562px;left:0;width:1200px;height:622px}
.authors .section-heading{top:82px}
.authors .lead-red{top:133px}
.author-card{position:absolute;left:262px;top:176px;width:678px;height:276px;background:#f3f3f3;box-shadow:0 8px 20px rgba(0,0,0,.18)}
.author-photo{position:absolute;left:0;top:0;width:237px;height:276px;background:linear-gradient(180deg,#6c7a83 0%,#8fa4b3 45%,#5d9ad6 100%)}
.author-name{position:absolute;left:263px;top:48px;font-size:21px;font-weight:400;color:var(--ink)}
.author-bio{position:absolute;left:263px;top:84px;width:390px;font-size:13px;line-height:24px}
.author-bio a{color:var(--ink);text-decoration:underline}
.slide-arrow{position:absolute;top:289px;width:24px;height:50px;background:#333;display:flex;align-items:center;justify-content:center}
.slide-arrow.prev{left:262px}
.slide-arrow.next{left:916px}
.authors .btn{left:501px;top:490px}

/* faq */
.faq{position:absolute;top:2184px;left:0;width:1200px;height:573px;background:linear-gradient(90deg,#f1f1f1,#fafafa 60%,#ececec)}
.faq-heading{position:absolute;left:88px;top:80px;display:flex;align-items:center;gap:18px;font-weight:800;font-size:32px;color:var(--ink)}
.faq-heading::before{content:"";width:78px;height:3px;background:var(--ink)}
.faq-bar{position:absolute;left:88px;width:585px;height:35px;display:flex;align-items:center;justify-content:space-between;padding:0 14px;color:var(--white);font-size:15px}
.faq-bar.open{top:132px;background:var(--ink)}
.faq-bar.closed{background:var(--bar-grey)}
.faq-answer{position:absolute;left:88px;top:184px;width:585px;font-size:13px;line-height:24px}
.faq .btn{left:88px;top:441px}
.faq-art{position:absolute;left:761px;top:121px;width:353px;height:331px;border-radius:40px;background:linear-gradient(135deg,#f05a86 0%,#e6426e 35%,#3ab0e0 60%,#8cbf2a 100%);opacity:.9}

/* cta */
.cta{position:absolute;top:2757px;left:0;width:1200px;height:221px;background:linear-gradient(180deg,var(--red) 0%,var(--red-mid) 70%,#d61c24 100%)}
.cta-title{position:absolute;top:34px;width:100%;text-align:center;color:var(--white);font-weight:800;font-size:32px}
.cta-sub{position:absolute;top:90px;width:100%;text-align:center;color:var(--white);font-size:19px}
.cta .btn{left:501px;top:137px}

/* footer */
.site-footer{position:absolute;top:2978px;left:0;width:1200px;height:331px;background:var(--footer);color:var(--footer-text);font-size:13px}
.foot-col{position:absolute;top:70px}
.foot-col h4{display:flex;align-items:center;gap:14px;color:var(--white);font-size:20px;font-weight:700;text-transform:uppercase;margin-bottom:14px}
.foot-col h4::before{content:"";width:32px;height:2px;background:var(--red)}
.col-about{left:88px;width:350px;line-height:24px}
.col-about p{width:300px}
.col-links{left:527px}
.link-grid{display:grid;grid-template-columns:124px 110px;row-gap:3px;line-height:21px}
.col-contact{left:862px;width:300px}
.contact-row{display:flex;align-items:flex-start;gap:12px;margin-bottom:10px;line-height:20px}
.contact-row svg{flex:none}
.foot-rule{position:absolute;left:88px;top:258px;width:1024px;height:1px;background:#3a3a3a}
.copyright{position:absolute;left:88px;top:287px;font-size:12px}
.social{position:absolute;right:88px;top:286px;display:flex;gap:14px}
.social span{width:16px;height:16px;border-radius:50%;background:var(--white)}
</style>
</head>
<body>

<header class="site-header">
  <div class="brand"><span class="brand-dot"></span>Redline Publishing</div>
  <nav class="main-nav">
    <span class="active">Home</span><span>About RLP</span><span>Apply Now</span><span>RLP Worlds</span><span>RLP Authors</span><span>FAQ</span><span>News</span><span>Contact Us</span>
  </nav>
</header>

<section class="hero" role="img" aria-label="Photograph of a rocket launch with billowing smoke clouds over water">
  <h1 class="hero-title">LOREM IPSUM IS SIMPLY DUMMY TEXT</h1>
  <div class="hero-video"><span class="brand-dot"></span>Redline Publishing</div>
  <span class="btn btn-red">Apply Now</span>
</section>

<section class="about">
  <h2 class="section-heading">About RLP</h2>
  <p class="lead-red">It is a long established fact that a reader will be distracted by the readable content of a page when looking at its layout.</p>
  <p class="about-copy">Lorem Ipsum is simply dummy text of the printing and typesetting industry. Lorem Ipsum has been the industry's standard dummy text ever since the 1500s, when an unknown printer took a galley of type and scrambled it to make a type specimen book. It has survived not only five centuries, but also the leap into electronic typesetting, remaining essentially unchanged. It was popularised in the 1960s with the release of Typeleaf sheets containing Lorem Ipsum passages, and more recently with desktop publishing software like Folio Layout including versions of Lorem Ipsum.</p>
  <span class="btn btn-outline">Read More</span>
</section>

<section class="featured">
  <div class="book-visual" role="img" aria-label="Illustrated book cover beside an open book spread"></div>
  <h3 class="featured-title">Lorem ipsum simple</h3>
  <p class="featured-copy">Lorem Ipsum is simply dummy text of the printing and typesetting industry. Lorem Ipsum has been the industry's standard dummy text ever since the 1500s, when an unknown printer took a galley of type and scrambled it to make a type specimen book. It has survived not only five centuries, but also the leap into electronic typesetting, remaining essentially... <a>READ MORE</a></p>
  <span class="btn btn-outline">View All</span>
</section>

<section class="authors">
  <h2 class="section-heading">RLP Authors</h2>
  <p class="lead-red">Lorem Ipsum is simply dummy text of the printing and typesetting industry.</p>
  <div class="author-card">
    <div class="author-photo" role="img" aria-label="Portrait photograph of the author"></div>
    <h3 class="author-name">John Doe</h3>
    <p class="author-bio">Lorem Ipsum is simply dummy text of the printing and typesetting industry. Lorem Ipsum has been the industry's standard dummy text ever since the 1500s, when an unknown printer took a galley of type and scrambled it to make a type specimen book. It has survived not only five centuries, but also the leap into electronic typesetting, remaining... <a>VIEW DETAILS</a></p>
  </div>
  <span class="slide-arrow prev"><svg width="8" height="12" viewBox="0 0 8 12"><path d="M7 1L2 6l5 5" fill="none" stroke="#fff" stroke-width="2"/></svg></span>
  <span class="slide-arrow next"><svg width="8" height="12" viewBox="0 0 8 12"><path d="M1 1l5 5-5 5" fill="none" stroke="#fff" stroke-width="2"/></svg></span>
  <span class="btn btn-outline">View All</span>
</section>

<section class="faq">
  <h2 class="faq-heading">FAQ</h2>
  <div class="faq-bar open"><span>Lorem Ipsum is simply dummy text of the printing and typesetting?</span><span>&minus;</span></div>
  <p class="faq-answer">Contrary to popular belief, Lorem Ipsum is not simply random text. It has roots in a piece of classical Latin literature from 45 BC, making it over 2000 years old. Tomas Verhoeven, a Latin professor at Alder Hill College in Vermont, looked up one of the more obscure Latin words, consectetur, from a Lorem Ipsum passage, and going through the cites of the word in classical literature, discovered the undoubtable source.</p>
  <div class="faq-bar closed" style="top:326px"><span>Where does it come from?</span><span>+</span></div>
  <div class="faq-bar closed" style="top:379px"><span>All the Lorem Ipsum generators on the Internet tend to repeat?</span><span>+</span></div>
  <span class="btn btn-outline">Read More</span>
  <div class="faq-art" role="img" aria-label="Illustration of colourful overlapping speech bubbles with question marks"></div>
</section>

<section class="cta">
  <h2 class="cta-title">LOREM IPSUM IS SIMPLY DUMMY TEXT</h2>
  <p class="cta-sub">It is a long established fact that a reader will be distracted by the readable content of a page.</p>
  <span class="btn btn-white">Apply Now</span>
</section>

<footer class="site-footer">
  <div class="foot-col col-about">
    <h4>About Us</h4>
    <p>Contrary to popular belief, Lorem Ipsum is not simply random text. It has roots in a piece of classical Latin literature from 45 BC, making it over 2000 years old, a Latin professor at Alder Hill.</p>
  </div>
  <div class="foot-col col-links">
    <h4>Quick Links</h4>
    <div class="link-grid">
      <span>Home</span><span>RLP Authors</span>
      <span>About RLP</span><span>FAQ</span>
      <span>Apply Now</span><span>News</span>
      <span>RLP Worlds</span><span>Contact us</span>
    </div>
  </div>
  <div class="foot-col col-contact">
    <h4>Contact Info</h4>
    <div class="contact-row">
      <svg width="20" height="20" viewBox="0 0 20 20"><circle cx="10" cy="10" r="10" fill="#fff"/><path d="M10 4a4 4 0 0 0-4 4c0 3 4 8 4 8s4-5 4-8a4 4 0 0 0-4-4z" fill="#ec1f27"/><circle cx="10" cy="8" r="1.5" fill="#fff"/></svg>
      <span>48 Harbor Lane, Westbrook,<br>USA 20418</span>
    </div>
    <div class="contact-row">
      <svg width="20" height="20" viewBox="0 0 20 20"><circle cx="10" cy="10" r="10" fill="#fff"/><path d="M6.5 5.5l2 0 1 2.5-1.3 1a6 6 0 0 0 2.8 2.8l1-1.3 2.5 1v2a1.5 1.5 0 0 1-1.5 1.3A8 8 0 0 1 5.2 7 1.5 1.5 0 0 1 6.5 5.5z" fill="#ec1f27"/></svg>
      <span>555 014 2290 &nbsp;/&nbsp; 555 018 7731</span>
    </div>
    <div class="contact-row">
      <svg width="20" height="20" viewBox="0 0 20 20"><circle cx="10" cy="10" r="10" fill="#fff"/><rect x="5" y="6.5" width="10" height="7" fill="#ec1f27"/><path d="M5 6.5l5 4 5-4" fill="none" stroke="#fff" stroke-width="1"/></svg>
      <span>info@redlinepublishing.com</span>
    </div>
  </div>
  <div class="foot-rule"></div>
  <p class="copyright">© Copyright 2018 &nbsp;|&nbsp; All Rights Reserved.</p>
  <div class="social"><span></span><span></span><span></span></div>
</footer>

</body>
</html>
```